Gin bottle designs - micro distillery

We are an Italian Distillery in Melbourne Australia. We would like to modernise the brand and in particular the bottle labels. We need to get a lable that will look better on the shelf while still maintaining the Italian "feel" of the product.

You can also refer to web site: www.verantocellars.com for a background.

At this time we are stuck with the rectangular bottles. We can consider different configurations (like a top label and a wrap around label at the bottom

The key message is more modern and attention grabbing.

Target Market(s)

Alcohol drinkers

Requirements
Must have
• GIN
Mediterranean Gin
Grappa
Brandy
Vodka

```html
<!DOCTYPE html>
<html lang="en">
<head>
<meta charset="utf-8">
<title>Veranto Spirits – Label Range</title>
<link rel="stylesheet" href="https://fonts.googleapis.com/css2?family=Bebas+Neue&family=IM+Fell+DW+Pica:ital@0;1&family=Open+Sans:wght@400;700&family=Special+Elite&display=swap">
<style>
  :root {
    --paper: #ffffff;
    --story-ink: #8a5f52;
    --gin-blue: #2f6b9a;
    --gin-ground: #e9edf4;
    --gin-ink: #7b8a9c;
    --graspa-red: #c46662;
    --graspa-ground: #f6ece7;
    --graspa-ink: #c46662;
    --brand-green: #3f8a3a;
    --glass: rgba(226, 233, 238, 0.55);
    --glass-edge: #c6cfd6;
    --cap: #1f1f22;
  }
  * { box-sizing: border-box; margin: 0; padding: 0; }
  html, body { width: 1200px; height: 720px; overflow: hidden; background: var(--paper); }
  .board { position: relative; width: 1200px; height: 720px; overflow: hidden; background: var(--paper); }

  /* Brand story column */
  .brand-mark {
    position: absolute; left: 56px; top: 120px; width: 150px;
    display: flex; align-items: center; justify-content: center; gap: 8px;
    font-family: "IM Fell DW Pica", serif; font-size: 28px; color: var(--brand-green);
    letter-spacing: 1px;
  }
  .brand-mark .dot { width: 14px; height: 14px; border-radius: 50%; background: var(--brand-green); flex: none; }
  .story {
    position: absolute; left: 56px; top: 256px; width: 212px;
    font-family: "Open Sans", sans-serif; font-size: 9.4px; line-height: 1.42; color: var(--story-ink);
  }
  .story p { margin-bottom: 13px; }

  /* Label */
  .label {
    position: absolute; width: 198px; height: 648px; overflow: hidden;
    box-shadow: 0 0 6px rgba(0,0,0,0.18);
    text-align: center;
  }
  .label--gin { background: var(--gin-ground); --accent: var(--gin-blue); --ink: var(--gin-ink); }
  .label--graspa { background: var(--graspa-ground); --accent: var(--graspa-red); --ink: var(--graspa-ink); }
  .label__brand {
    position: absolute; top: 56px; left: 0; right: 0;
    display: flex; align-items: center; justify-content: center; gap: 5px;
    font-family: "IM Fell DW Pica", serif; font-size: 17px; color: var(--brand-green);
  }
  .label__brand .dot { width: 8px; height: 8px; border-radius: 50%; background: var(--brand-green); }
  .label__tagline {
    position: absolute; top: 128px; left: 0; right: 0;
    font-family: "IM Fell DW Pica", serif; font-style: italic; font-size: 18px; line-height: 21px; color: var(--ink);
  }
  .label__art {
    position: absolute; left: 38px; top: 178px; width: 124px; height: 300px;
    border-radius: 45% 45% 50% 50%;
    opacity: 0.35;
  }
  .label--gin .label__art { background: radial-gradient(ellipse at 50% 45%, #9aa3b0, #dde2ea 75%); }
  .label--graspa .label__art { background: radial-gradient(ellipse at 50% 45%, #d9a08c, #f1e0d8 75%); }
  .label__name {
    position: absolute; left: 0; right: 0;
    font-family: "Bebas Neue", sans-serif; color: var(--accent); line-height: 0.9;
    text-shadow: 2px 2px 0 #fff, 4px 4px 0 rgba(60,60,60,0.35);
  }
  .label--gin .label__name { top: 214px; font-size: 150px; letter-spacing: 2px; }
  .label--graspa .label__name { top: 226px; font-size: 64px; letter-spacing: 1px; }
  .label__seal {
    position: absolute; left: 120px; top: 392px; width: 70px; height: 70px; border-radius: 50%;
    border: 3px double var(--accent); background: rgba(255,255,255,0.6);
  }
  .label__origin {
    position: absolute; top: 460px; left: 0; right: 0;
    font-family: "IM Fell DW Pica", serif; font-style: italic; font-size: 15px; line-height: 18px; color: var(--ink);
  }
  .label--graspa .label__origin { top: 474px; font-size: 16px; }
  .label__batch {
    position: absolute; top: 506px; left: 0; right: 0;
    font-family: "Open Sans", sans-serif; font-size: 8px; color: #666;
  }
  .label__batch strong {
    display: block; font-family: "Special Elite", monospace; font-weight: 400; font-size: 14px;
    letter-spacing: 2px; color: #555;
  }
  .label__band {
    position: absolute; left: 0; right: 0; bottom: 0; height: 108px; padding: 14px 12px 0;
    background: var(--accent); color: #fff;
    font-family: "IM Fell DW Pica", serif; font-style: italic; font-size: 13px; line-height: 16px;
  }
  .label__measures {
    position: absolute; left: 16px; right: 16px; bottom: 12px;
    display: flex; justify-content: space-between;
    font-family: "IM Fell DW Pica", serif; font-style: normal; font-size: 12px;
  }

  /* Bottles */
  .bottle { position: absolute; top: 42px; width: 192px; height: 662px; }
  .bottle svg { position: absolute; inset: 0; }
  .bottle .label { left: 17px; top: 138px; transform: scale(0.8); transform-origin: 0 0; box-shadow: none; }
</style>
</head>
<body>
<main class="board">

  <div class="brand-mark"><span class="dot"></span>VERANTO</div>

  <section class="story">
    <p>The VERANTO story dates back to the American Prohibition. My grandfather Matteo Corradin was a steelworker in Vernon Hill, Chicago. He went there to work and send money back to his family in Calvene, Italy. During his visits back to Italy, he would be asked where he worked. Vernon Hill was quickly Italianised to Veranto, which became the family's nickname.</p>
    <p>Calvene lies in the Northern part of Italy, near Bassano del Grappa, an area known for its rugged terrain, heavy snow, great food and grappa.</p>
    <p>In his spare time, Matteo would use scrap metal from the steelworks to make moonshine stills for his relatives and friends.</p>
    <p>I use traditional techniques together with a modern, computerised still to make the VERANTO spirits in honour of my grandfather.</p>
  </section>

  <!-- Flat labels -->
  <article class="label label--gin" style="left:280px; top:48px;">
    <div class="label__brand"><span class="dot"></span>VERANTO</div>
    <p class="label__tagline">Italian Heritage<br>Aussie Spirit</p>
    <div class="label__art" role="img" aria-label="Engraved grape bunch and vine leaf illustration"></div>
    <h2 class="label__name">GIN</h2>
    <div class="label__seal"></div>
    <p class="label__origin">Made from Premium<br>Australian Grape Spirit</p>
    <p class="label__batch">Batch/Lotto.<strong>UNO(00)</strong></p>
    <div class="label__band">
      Distilled with Lavender,<br>Rosemary, Fennel &amp; other select<br>Mediterranean Botanicals
      <div class="label__measures"><span>500ml</span><span>45% Alc/Vol</span></div>
    </div>
  </article>

  <article class="label label--graspa" style="left:530px; top:48px;">
    <div class="label__brand"><span class="dot"></span>VERANTO</div>
    <p class="label__tagline">Italian Heritage<br>Aussie Spirit</p>
    <div class="label__art" role="img" aria-label="Engraved grape bunch and vine leaf illustration"></div>
    <h2 class="label__name">GRASPA<br>VERANTO</h2>
    <div class="label__seal"></div>
    <p class="label__origin">Distillato di Cabernet</p>
    <p class="label__batch">Batch/Lotto.<strong>PRIMA</strong></p>
    <div class="label__band">
      Aged in a rare ex fortified<br>Botrytis Semillon barrel
      <div class="label__measures"><span>500ml</span><span>45% Alc/Vol</span></div>
    </div>
  </article>

  <!-- Bottles -->
  <div class="bottle" style="left:756px;">
    <svg viewBox="0 0 192 662" width="192" height="662" aria-hidden="true">
      <path d="M66 48 L66 92 Q66 112 32 122 Q10 128 10 152 L10 652 Q10 660 18 660 L174 660 Q182 660 182 652 L182 152 Q182 128 160 122 Q126 112 126 92 L126 48 Z" fill="var(--glass)" stroke="var(--glass-edge)" stroke-width="2"/>
      <rect x="62" y="0" width="68" height="50" rx="5" fill="var(--cap)"/>
    </svg>
    <article class="label label--gin">
      <div class="label__brand"><span class="dot"></span>VERANTO</div>
      <p class="label__tagline">Italian Heritage<br>Aussie Spirit</p>
      <div class="label__art" role="img" aria-label="Engraved grape bunch and vine leaf illustration"></div>
      <h2 class="label__name">GIN</h2>
      <div class="label__seal"></div>
      <p class="label__origin">Made from Premium<br>Australian Grape Spirit</p>
      <p class="label__batch">Batch/Lotto.<strong>UNO(00)</strong></p>
      <div class="label__band">
        Distilled with Lavender,<br>Rosemary, Fennel &amp; other select<br>Mediterranean Botanicals
        <div class="label__measures"><span>500ml</span><span>45% Alc/Vol</span></div>
      </div>
    </article>
  </div>

  <div class="bottle" style="left:958px;">
    <svg viewBox="0 0 192 662" width="192" height="662" aria-hidden="true">
      <path d="M66 48 L66 92 Q66 112 32 122 Q10 128 10 152 L10 652 Q10 660 18 660 L174 660 Q182 660 182 652 L182 152 Q182 128 160 122 Q126 112 126 92 L126 48 Z" fill="var(--glass)" stroke="var(--glass-edge)" stroke-width="2"/>
      <rect x="62" y="0" width="68" height="50" rx="5" fill="var(--cap)"/>
    </svg>
    <article class="label label--graspa">
      <div class="label__brand"><span class="dot"></span>VERANTO</div>
      <p class="label__tagline">Italian Heritage<br>Aussie Spirit</p>
      <div class="label__art" role="img" aria-label="Engraved grape bunch and vine leaf illustration"></div>
      <h2 class="label__name">GRASPA<br>VERANTO</h2>
      <div class="label__seal"></div>
      <p class="label__origin">Distillato di Cabernet</p>
      <p class="label__batch">Batch/Lotto.<strong>PRIMA</strong></p>
      <div class="label__band">
        Aged in a rare ex fortified<br>Botrytis Semillon barrel
        <div class="label__measures"><span>500ml</span><span>45% Alc/Vol</span></div>
      </div>
    </article>
  </div>

</main>
</body>
</html>
```